Bravenix Website Design
Bravenix Website
@JW,
uploaded revised drafts Please check your private message.
ToruVin
yes sure i would bring some more designs for you.
Thanks
Hello,
Can I get more design incorporating orange and green ? (or any color that would represent solar)
WHY JW ISN'T REPLYING?
IT'S BEEN 2 DAYS.
Submitted my drafts for the project.Please feel free to let me know the required changes so that your expectations are met. Awaiting for your kind feedback
Hi JW
Do you have logo on your website? And I would to ask further info in your website.

```html
<!DOCTYPE html>
<html lang="en">
<head>
<meta charset="utf-8">
<title>Bravenix Website</title>
<link rel="stylesheet" href="https://fonts.googleapis.com/css2?family=Arimo:wght@400;700&display=swap">
<style>
:root{
  --header-dark:#3a1016;
  --header-mid:#5a1a1e;
  --hero-hot:#e4571a;
  --hero-deep:#a8280f;
  --hero-edge:#6e1a12;
  --white:#ffffff;
  --nav-divider:#7a3a3a;
  --page-bg:#f4f4f4;
  --body-text:#6a6a6a;
  --heading-text:#333333;
  --dot-off:#8a3420;
  --dot-on:#f3c6a6;
  --arrow-bg:#f7a31c;
  --icon-green:#3d9a3a;
  --icon-red:#b3412a;
  --icon-blue:#2d77c4;
  --screen-frame:#d9d9d9;
}
*{margin:0;padding:0;box-sizing:border-box}
html,body{width:1200px;height:694px;overflow:hidden}
body{font-family:"Arimo",Arial,sans-serif;background:var(--page-bg);position:relative}
.site-header{position:absolute;left:0;top:0;width:1200px;height:96px;
  background:linear-gradient(180deg,var(--header-mid),var(--header-dark));}
.brand-name{position:absolute;left:60px;top:22px;font-size:44px;font-weight:700;color:var(--white);letter-spacing:1px}
.main-nav{position:absolute;right:60px;top:36px;display:flex;font-size:15px;color:var(--white)}
.main-nav a{color:var(--white);text-decoration:none;padding:0 14px;border-left:1px solid var(--nav-divider)}
.main-nav a:first-child{border-left:none}
.main-nav a.current{text-decoration:underline}
.hero{position:absolute;left:0;top:96px;width:1200px;height:396px;
  background:radial-gradient(ellipse 70% 90% at 30% 40%,var(--hero-hot),var(--hero-deep) 65%,var(--hero-edge));}
.hero-title{position:absolute;left:65px;top:44px;width:520px;font-size:28px;line-height:34px;font-weight:700;color:var(--white)}
.hero-copy{position:absolute;left:65px;top:140px;width:530px;font-size:15.5px;line-height:21px;color:var(--white)}
.hero-shot{position:absolute;left:629px;top:36px;width:408px;height:324px;border:4px solid var(--screen-frame);
  background:linear-gradient(160deg,#f5f5f5,#e6e6e6);}
.slider-dots{position:absolute;left:68px;top:368px;display:flex;gap:8px}
.slider-dots span{width:10px;height:10px;border-radius:50%;background:var(--dot-off)}
.slider-dots span:first-child{background:var(--dot-on)}
.slider-arrows{position:absolute;left:665px;top:362px;display:flex;gap:8px}
.features{position:absolute;left:0;top:492px;width:1200px;height:202px;background:var(--page-bg)}
.feature{position:absolute;top:22px;width:330px}
.feature h2{font-size:19px;font-weight:700;color:var(--heading-text);display:flex;align-items:center;gap:10px;margin-bottom:10px}
.feature p{font-size:13px;line-height:19.5px;color:var(--body-text)}
</style>
</head>
<body>
<header class="site-header">
  <div class="brand-name">Bravenix</div>
  <nav class="main-nav">
    <a href="#">Home</a><a href="#">Our Blog</a><a href="#">Media Gallery</a><a href="#">Testing the Elements</a><a href="#">About ▾</a><a href="#" class="current">Services</a>
  </nav>
</header>

<section class="hero">
  <h1 class="hero-title">So, Whats that featured slider all about?</h1>
  <p class="hero-copy">Using theme options panel, you can set "most recent posts", any post "based on category" or "based on a specific -user defined- tag" here on featured slider. Another cool feature of featured slider is auto rotation support. By a single check on theme's advanced options panel you can whether disable or enable auto rotation support for this slider. Mauris lectus nisl, consequat consectetur egestas nec, sodales non lectus.</p>
  <div class="hero-shot" role="img" aria-label="Screenshot of the theme in a browser window"></div>
  <div class="slider-dots"><span></span><span></span><span></span><span></span><span></span><span></span></div>
  <div class="slider-arrows">
    <svg width="24" height="24" viewBox="0 0 24 24"><circle cx="12" cy="12" r="11" fill="var(--arrow-bg)"/><path d="M14 7l-5 5 5 5" stroke="#fff" stroke-width="2.5" fill="none"/></svg>
    <svg width="24" height="24" viewBox="0 0 24 24"><circle cx="12" cy="12" r="11" fill="var(--arrow-bg)"/><path d="M10 7l5 5-5 5" stroke="#fff" stroke-width="2.5" fill="none"/></svg>
  </div>
</section>

<section class="features">
  <article class="feature" style="left:65px">
    <h2><svg width="20" height="20" viewBox="0 0 20 20"><path d="M2 7h8V2l8 8-8 8v-5H2z" fill="var(--icon-green)"/></svg>Brand Orientation</h2>
    <p>Brand orientation is a deliberate approach to working with brands, both internally and externally. The most important driving force behind this increased interest in strong brands is the accelerating pace of globalization</p>
  </article>
  <article class="feature" style="left:444px">
    <h2><svg width="20" height="20" viewBox="0 0 20 20"><circle cx="10" cy="10" r="9" fill="var(--icon-red)"/><path d="M10 4v12M4 10h12" stroke="#fff" stroke-width="2.5"/></svg>Support and Resistance</h2>
    <p>A support level is a price level where the price tends to find support as it is going down. This means the price is more likely to bounce off this level rather than break through it. Resistance level is the opposite of a support level</p>
  </article>
  <article class="feature" style="left:780px">
    <h2><svg width="20" height="20" viewBox="0 0 20 20"><circle cx="10" cy="10" r="7" fill="none" stroke="var(--icon-blue)" stroke-width="4" stroke-dasharray="3 2.5"/><circle cx="10" cy="10" r="4.5" fill="var(--icon-blue)"/><circle cx="10" cy="10" r="2" fill="#fff"/></svg>Incompatibility Thesis</h2>
    <p>Incompatibility thesis is in an argument in research methodology about incompatibility of quantitative research and qualitative research paradigms in the same research. This thesis is based on philosophies of post-structuralism.</p>
  </article>
</section>
</body>
</html>
```